Einfache Webside für kleine Promotion- und Personalagentur
Zielgruppe
Lumo Staffing ist eine international tätige Promotion- und Personalagentur. Wir bieten auch im Bereich Sport der jew. Sportart affine Hostessen und Hosts f an.
Aufgabenstellung
Wir hatten bis dato eine sehr gute Auftragslage und leider keine Zeit für eine Homepage. Wir suchen jemaden der uns das Design für die Seite übernimmt und Online stellt. Wir sind auch offen wenn dies über z.B. Q+Z erfolgt. Auf den jeweiligen Seiten wollen wir den Text dann immer selbst eintragen. Seiten: Startseite mit Buttons zu folgenden Feldern: Promotion (Text mit Erklärung was wir machen und Bildern), Personal (Text mit Erklärung was wir machen und Bilder - die Bilder sollten austauschbar sein), Team, Referenzen, Kontaktseite, Gästebuch, Impressum. Die Seite sollte Modern aussehen und nicht zu überladen sein.

```html
<!DOCTYPE html>
<html lang="en">
<head>
<meta charset="utf-8">
<title>Lumo Staffing – International Promotion &amp; HR Services</title>
<link href="https://fonts.googleapis.com/css2?family=Open+Sans:wght@400;600;700&family=Questrial&display=swap" rel="stylesheet">
<style>
:root{
  --blue:#1a8fd8;
  --blue-deep:#1e63c4;
  --nav:#8a9aa8;
  --nav-dark:#7a8a98;
  --gray-band:#7b7b7b;
  --text:#8a8a8a;
  --heading:#1b1b1b;
  --light-blue:#b5d6fa;
  --orange:#f5793b;
  --footer:#3a3a3a;
  --footer-dark:#262626;
}
*{margin:0;padding:0;box-sizing:border-box}
html,body{width:1200px;height:2837px;overflow:hidden;background:#fff}
body{font-family:"Open Sans",sans-serif;color:var(--text);position:relative}
.section{position:absolute;left:0;width:1200px}
.wrap{position:absolute;left:100px;width:1000px}
h2{font-family:"Questrial",sans-serif;font-weight:400;color:var(--heading)}

/* header */
.header{top:0;height:103px}
.brand{position:absolute;left:100px;top:30px;display:flex;align-items:center;gap:10px}
.brand-dot{width:40px;height:40px;border-radius:50%;background:var(--blue)}
.brand-name{font-family:"Questrial",sans-serif;font-size:24px;color:var(--blue)}
.tagline{position:absolute;left:100px;top:84px;font-size:8px;color:#999}
.util{position:absolute;top:44px;left:615px;display:flex;gap:28px;font-size:14px;color:#333;align-items:center}
.caret{display:inline-block;border:5px solid transparent;border-top:6px solid #333;margin-left:6px;vertical-align:-3px}
.lang{position:absolute;left:928px;top:40px;width:144px;height:24px;border:1px solid #bbb;background:#f4f4f4;font-size:12px;color:#333;padding:3px 6px;display:flex;gap:6px;align-items:center}
.flag{width:22px;height:13px;background:#2a3c8f}
.lang .caret{position:absolute;right:6px;top:7px;border-width:4px;border-top-width:5px;margin:0}

/* nav */
.nav{top:103px;height:43px;background:linear-gradient(#98a8b5,var(--nav-dark))}
.nav ul{position:absolute;left:100px;display:flex;list-style:none;height:43px}
.nav li{color:#fff;font-size:16px;text-align:center;line-height:43px;border-right:1px solid #9fafbb}
.nav li.active{background:var(--blue)}
.nav li:last-child{border:none}

/* hero */
.hero{top:146px;height:470px;background:linear-gradient(90deg,#e8ecef 0%,#cdd6dc 35%,#eef1f3 60%,#c9d7e6 100%)}
.caption{position:absolute;left:100px;top:293px;width:499px;height:129px;background:rgba(30,99,196,.88);color:#fff;font-size:31px;line-height:39px;padding:14px 8px}
.dots{position:absolute;left:125px;top:439px;display:flex;gap:5px}
.dots span{width:15px;height:15px;border-radius:50%;background:var(--blue-deep)}
.dots span.on{background:#fff}

/* welcome */
.welcome{top:616px;height:333px}
.welcome h2{position:absolute;left:100px;top:34px;font-size:34px}
.welcome p{position:absolute;left:100px;width:980px;font-size:16px;line-height:28px}

/* about */
.about{top:949px;height:543px;background:var(--gray-band);color:#fff}
.about h2{position:absolute;left:100px;top:44px;font-size:34px}
.about .lead{position:absolute;left:100px;top:94px;width:980px;font-size:16.5px;line-height:28px}
.card{position:absolute;top:186px;width:314px}
.card .photo{height:182px;background:linear-gradient(135deg,#e9eaec,#a9b0b8)}
.card.hi .photo{outline:2px solid var(--blue);outline-offset:-2px;background:linear-gradient(135deg,#dfe4ea,#8f9aa6)}
.card.dark .photo{background:linear-gradient(135deg,#2b2f36,#7a7c80)}
.card h3{font-family:"Open Sans",sans-serif;font-weight:400;font-size:22px;margin-top:10px}
.card p{font-size:12.5px;line-height:18px;margin-top:6px}

/* jobs/news */
.lists{top:1492px;height:368px}
.lists h2{position:absolute;top:42px;font-size:34px}
.job{position:absolute;left:100px;width:400px}
.job .t{font-family:"Questrial",sans-serif;font-size:21px;color:#777;padding-left:22px;position:relative}
.job .t:before{content:"";position:absolute;left:0;top:8px;width:12px;height:12px;border-radius:50%;background:#aaa}
.job .l{font-family:"Questrial",sans-serif;color:var(--blue);font-size:17px;padding-left:22px;margin-top:2px}
.job .d{font-size:13px;color:#777;padding-left:22px;margin-top:8px}
.rule{position:absolute;border-top:2px dotted #999}
.news{position:absolute;left:638px;width:462px;height:100px}
.news .day{position:absolute;left:0;top:0;font-size:58px;font-weight:700;color:#333;line-height:60px;letter-spacing:2px}
.news .mon{position:absolute;left:8px;top:62px;font-size:20px;color:#666}
.news .h{position:absolute;left:85px;top:0;font-family:"Questrial",sans-serif;font-size:17px;color:var(--blue)}
.news .x{position:absolute;left:85px;top:30px;font-size:13px;line-height:20px;color:#777;width:380px}

/* contact */
.contact{top:1860px;height:280px;background:var(--light-blue)}
.contact h2{position:absolute;top:49px;font-size:34px}
.info{position:absolute;left:100px;display:flex;gap:18px;align-items:center;font-size:14px;color:#222}
.info svg{width:24px;flex:none}
.field{position:absolute;height:36px;background:#fff;border:1px solid #d5d5d5;font-size:14px;color:#aaa;padding:8px 10px}
.btn{position:absolute;height:34px;color:#fff;font-weight:700;font-size:18px;text-align:center;line-height:34px;top:170px}

/* success */
.success{top:2140px;height:382px}
.success h2{position:absolute;top:52px;width:1200px;text-align:center;font-family:"Open Sans",sans-serif;font-size:32px;color:var(--blue)}
.success p{position:absolute;left:210px;top:96px;width:780px;text-align:center;font-size:16px;line-height:28px;color:#444}
.arrow{position:absolute;top:122px;width:20px;height:20px;border-radius:50%;border:2px solid #ccc;background:#eee}
.avatar{position:absolute;left:511px;top:225px;width:125px;height:125px;border-radius:50%;border:2px solid var(--blue);background:linear-gradient(#eef3f8,#c8d2dc)}
.who{position:absolute;left:649px;top:258px;font-size:21px;color:#555}
.when{position:absolute;left:652px;top:290px;font-size:16px;font-style:italic;color:var(--blue)}

/* social band */
.feed{top:2522px;height:188px;background:linear-gradient(#2d95de,#1a86d2)}
.feed .name{position:absolute;top:34px;width:1200px;text-align:center;font-family:"Open Sans",sans-serif;font-weight:700;font-size:34px;color:#fff}
.feed p{position:absolute;left:130px;top:100px;width:940px;text-align:center;color:#fff;font-size:16px;line-height:28px}

/* footer */
.foot{top:2710px;height:74px;background:var(--footer)}
.foot ul{list-style:none;display:flex;justify-content:center;gap:16px;margin-top:30px;font-size:11.5px;color:#fff;font-weight:600}
.foot li.sep{color:#bbb;font-weight:400}
.base{top:2784px;height:53px;background:var(--footer-dark)}
.base .copy{position:absolute;width:1200px;text-align:center;top:18px;font-size:11px;color:#fff}
.social{position:absolute;left:950px;top:14px;display:flex;gap:8px}
.social span{width:26px;height:26px;border-radius:50%;background:#ddd}
</style>
</head>
<body>

<header class="section header">
  <div class="brand"><span class="brand-dot"></span><span class="brand-name">Lumo Staffing</span></div>
  <div class="tagline">International Promotion &amp; HR services</div>
  <div class="util"><span>Sign in<i class="caret"></i></span><span>Register<i class="caret"></i></span><span>Select Language</span></div>
  <div class="lang"><span class="flag"></span>English<i class="caret"></i></div>
</header>

<nav class="section nav">
  <ul>
    <li class="active" style="width:109px">HOME</li>
    <li style="width:151px">ABOUT US</li>
    <li style="width:130px">TALENT</li>
    <li style="width:166px">COMPANIES</li>
    <li style="width:104px">JOBS</li>
    <li style="width:131px">EVENTS</li>
    <li style="width:173px">CONTACT US</li>
  </ul>
</nav>

<section class="section hero" role="img" aria-label="Photo of three smiling young professionals in business attire in an office">
  <div class="caption">Access a Network of Highy Qualified Young Professionals</div>
  <div class="dots"><span></span><span class="on"></span><span></span><span></span></div>
</section>

<section class="section welcome">
  <h2>Welcome to Lumo Staffing</h2>
  <p style="top:90px">Lorem ipsum dolor sit amet, consectetuer adipiscing elit, sed diam nonummy nibh euismod tincidunt ut laoreet dolore magna aliquam erat volutpat. Ut wisi enim ad minim veniam, quis nostrud exerci tation ullamcorper suscipit lobortis nisl ut aliquip ex ea commodo consequat. Duis autem vel eum iriure dolor in hendrerit in vulputate velit esse molestie</p>
  <p style="top:202px">Lorem ipsum dolor sit amet, consectetuer adipiscing elit, sed diam nonummy nibh euismod tincidunt ut laoreet dolore magna aliquam erat volutpat. Ut wisi enim ad minim veniam, quis nostrud exerci tation ullamcorper suscipit lobortis nisl ut aliquip ex ea commodo consequat. Duis autem vel eum iriure dolor in hendrerit in vulputate velit esse molestie</p>
</section>

<section class="section about">
  <h2 style="color:#111">About us</h2>
  <p class="lead">Lorem ipsum dolor sit amet, consectetuer adipiscing elit, sed diam nonummy nibh euismod tincidunt ut laoreet dolore magna aliquam erat volutpat. Ut wisi enim ad minim veniam, quis nostrud exerci tation</p>
  <div class="card" style="left:100px">
    <div class="photo" role="img" aria-label="Photo of a presenter speaking to a seated audience"></div>
    <h3>Our Vision</h3>
    <p>Lorem ipsum dolor sit amet, consectetuer adipiscing elit, sed diam nonummy nibh euismod tincidunt ut laoreet dolore magna aliquam</p>
  </div>
  <div class="card hi" style="left:444px">
    <div class="photo" role="img" aria-label="Photo of a diverse group of colleagues"></div>
    <svg style="position:absolute;left:134px;top:68px" width="48" height="48" viewBox="0 0 48 48"><circle cx="24" cy="24" r="24" fill="#1a8fd8"/><path d="M24 13v22M13 24h22" stroke="#fff" stroke-width="3"/></svg>
    <svg style="position:absolute;left:290px;top:182px" width="24" height="24" viewBox="0 0 24 24"><path d="M0 0h24v24z" fill="#1e63c4"/></svg>
    <h3>Our Mission</h3>
    <p>Lorem ipsum dolor sit amet, consectetuer adipiscing elit, sed diam nonummy nibh euismod tincidunt ut laoreet dolore magna aliquam</p>
  </div>
  <div class="card dark" style="left:786px">
    <div class="photo" role="img" aria-label="Photo of call centre staff wearing headsets"></div>
    <h3>Our Solution</h3>
    <p>Lorem ipsum dolor sit amet, consectetuer adipiscing elit, sed diam nonummy nibh euismod tincidunt ut laoreet dolore magna aliquam</p>
  </div>
</section>

<section class="section lists">
  <h2 style="left:100px">Latest Jobs</h2>
  <h2 style="left:638px">News &amp; Events</h2>
  <div class="job" style="top:112px"><div class="t">Website Designer</div><div class="l">Lorem &nbsp;Germany</div><div class="d">Lorem ipsum dolor sit amet, consectetuer adipiscing</div></div>
  <div class="rule" style="left:102px;top:207px;width:398px"></div>
  <div class="job" style="top:245px"><div class="t">Website Designer</div><div class="l">Lorem &nbsp;Germany</div><div class="d">Lorem ipsum dolor sit amet, consectetuer adipiscing</div></div>
  <div class="news" style="top:112px"><div class="day">15</div><div class="mon">NOV.</div><div class="h">Lorem &nbsp;Ipsum dolor site amet</div><div class="x">Lorem ipsum dolor sit amet, consectetuer adipiscing elit,sed adipiscing elit,sed diam sed diam...</div></div>
  <div class="rule" style="left:638px;top:212px;width:462px"></div>
  <div class="news" style="top:234px"><div class="day">15</div><div class="mon">NOV.</div><div class="h">Lorem &nbsp;Ipsum dolor site amet</div><div class="x">Lorem ipsum dolor sit amet, consectetuer adipiscing elit,sed adipiscing elit,sed diam sed diam...</div></div>
</section>

<section class="section contact">
  <h2 style="left:100px">Contact Details</h2>
  <h2 style="left:592px">Get in Touch With Us</h2>
  <div class="info" style="top:112px"><svg viewBox="0 0 24 32" height="32"><path d="M12 0C5 0 1 5 1 11c0 8 11 21 11 21s11-13 11-21C23 5 19 0 12 0z" fill="#111"/></svg><span>Lorem ipsum dolor sit amet<br>consetetur sadipscing</span></div>
  <div class="info" style="top:166px"><svg viewBox="0 0 24 24" height="24"><path d="M18 2l4 4-3 4c-2 5-6 9-11 11l-4 3-3-4 5-4 3 2c2-1 4-3 5-5l-2-3z" fill="#111"/></svg><span>(xxx) xxxx xxxx</span></div>
  <div class="info" style="top:205px"><svg viewBox="0 0 24 16" height="16"><rect width="24" height="16" fill="#111"/><path d="M1 1l11 8 11-8" stroke="#fff" stroke-width="1.5" fill="none"/></svg><span>info@lumo-staffing.de</span></div>
  <div class="field" style="left:589px;top:115px;width:243px">Your Name</div>
  <div class="field" style="left:854px;top:115px;width:247px">Email address</div>
  <div class="field" style="left:589px;top:169px;width:243px">Upload Your C V</div>
  <div class="btn" style="left:854px;width:112px;background:var(--blue)">UPLOAD</div>
  <div class="btn" style="left:989px;width:112px;background:var(--orange)">SUBMIT</div>
</section>

<section class="section success">
  <h2>Success Stories</h2>
  <span class="arrow" style="left:140px"></span>
  <span class="arrow" style="left:1036px"></span>
  <p>Lorem ipsum dolor sit amet, consectetuer adipiscing elit, sed diam nonummy nibh euismod tincidunt ut laoreet dolore magna aliquam erat volutpat. Ut wisi enim ad minim veniam, quis nostrud exerci tation ullamcorper suscipit lobortis nisl ut aliquip ex ea commodo consequat. Duis autem vel eum iriure dolor Duis autem vel eum iriure dolor in hendrerit in vulputate velit esse molestie</p>
  <div class="avatar" role="img" aria-label="Portrait photo of a smiling client"></div>
  <div class="who">Lorem ipsum</div>
  <div class="when">15, Nov. 2014</div>
</section>

<section class="section feed" role="region" aria-label="Latest social post">
  <div class="name">Chirpline</div>
  <p>Lorem ipsum dolor sit amet, consectetuer adipiscing elit, sed diam nonummy nibh euismod tincidunt ut laoreet dolore magna aliquam erat volutpat. Ut wisi enim ad minim veniam, quis nostrud exerci tation (1 day ago)</p>
</section>

<footer class="section foot">
  <ul>
    <li>About Us</li><li class="sep">/</li><li>Terms &amp; Conditions</li><li class="sep">/</li><li>Privacy Policy</li><li class="sep">/</li><li>Resources</li><li class="sep">/</li><li>Careers With Us</li><li class="sep">/</li><li>Jobs</li><li class="sep">/</li><li>Blog</li>
  </ul>
</footer>
<div class="section base">
  <div class="copy">Copyright © 2014 lumo-staffing. All rights reserved.</div>
  <div class="social"><span></span><span></span><span></span><span></span></div>
</div>

</body>
</html>
```